Brightquarry.com home page

On the existing home page I want to eliminate people in circles and promote these three earning opportunities:
1." Make a referral to existing advertiser"
Earn up to $5000 when you make a successful referral to one of our advertisers.
2."Sign up a new business to offer referral commisions to ambassaadors". Earn up to $5000 or more when you earn 5% of money paid out by business in referral fees.
3."Sign up new ambassadors"
Earn up to $5000 or more when you earn 5% of the money the ambassadors you sign up earn.

In each offer I want a learn more button .

Business

Serif

```html
<!DOCTYPE html>
<html lang="en">
<head>
<meta charset="utf-8">
<title>Brightquarry.com – Referral Marketplace</title>
<link href="https://fonts.googleapis.com/css2?family=Lato:wght@400;700&family=Open+Sans:wght@400;700&family=Roboto:wght@400;500;700&display=swap" rel="stylesheet">
<style>
  :root {
    --green: #27ae60;
    --green-dark: #0b6b10;
    --ink: #111;
    --heading: #2b2b2b;
    --muted: #8a8a8a;
    --nav-text: #555;
    --navy: #14365c;
    --rule: #e4e4e4;
    --tile-fill: #eef0ef;
  }
  * { box-sizing: border-box; margin: 0; padding: 0; }
  html, body { width: 1200px; height: 684px; overflow: hidden; background: #fff; }
  body { position: relative; font-family: "Lato", sans-serif; color: var(--ink); }

  .site-header { position: absolute; top: 0; left: 0; width: 1200px; height: 68px; background: #fff; }
  .brand { position: absolute; left: 98px; top: 13px; font-family: "Roboto", sans-serif; font-weight: 700; font-size: 33px; color: var(--green); letter-spacing: -0.5px; }
  .main-nav { position: absolute; top: 0; left: 729px; height: 68px; display: flex; }
  .main-nav a { display: block; height: 68px; line-height: 68px; font-family: "Open Sans", sans-serif; font-size: 13.5px; color: var(--nav-text); text-decoration: none; padding: 0 14px; }
  .main-nav a.is-active { background: var(--green); color: #fff; width: 63px; text-align: center; }

  .hero { position: absolute; top: 68px; left: 0; width: 1200px; height: 420px; background: linear-gradient(#f0f2f4 0, #fff 110px); }
  .hero-title { position: absolute; top: 18px; width: 100%; text-align: center; font-family: "Roboto", sans-serif; font-weight: 700; font-size: 36px; letter-spacing: 3px; color: var(--ink); }
  .hero-subtitle { position: absolute; top: 58px; width: 100%; text-align: center; font-family: "Roboto", sans-serif; font-weight: 400; font-size: 25.5px; letter-spacing: 0.6px; color: var(--heading); }

  .offer { position: absolute; top: 123px; width: 300px; height: 280px; text-align: center; }
  .offer-1 { left: 131px; } .offer-2 { left: 458px; } .offer-3 { left: 785px; }
  .offer-tile { width: 116px; height: 101px; margin: 0 auto; border: 2px solid #333; background: #fff; padding: 5px; }
  .offer-tile span { display: block; width: 100%; height: 100%; background: var(--tile-fill); }
  .offer-title { margin-top: 21px; font-weight: 700; font-size: 14px; line-height: 17px; color: var(--ink); text-transform: uppercase; }
  .offer-text { margin-top: 6px; font-size: 13.5px; line-height: 17.5px; color: var(--muted); }
  .learn-more { position: absolute; left: 56px; width: 188px; height: 46px; border: 2px solid var(--green); color: var(--green); font-size: 16px; display: flex; align-items: center; justify-content: center; gap: 8px; text-decoration: none; }
  .learn-more svg { width: 14px; height: 14px; fill: currentColor; }
  .learn-more--dark { border-color: #333; color: #222; }
  .offer-1 .learn-more { top: 206px; }
  .offer-2 .learn-more { top: 223px; }
  .offer-3 .learn-more { top: 208px; }

  .payout { position: absolute; top: 488px; left: 0; width: 1200px; height: 64px; border-top: 1px solid var(--rule); display: flex; align-items: center; justify-content: center; gap: 16px; background: #fff; }
  .payout-label { font-family: "Open Sans", sans-serif; font-size: 30px; color: var(--navy); }
  .payout-amount { font-family: "Open Sans", sans-serif; font-weight: 700; font-size: 40px; color: var(--green-dark); }

  .signup-band { position: absolute; top: 552px; left: 0; width: 1200px; height: 70px; background: var(--green); }
  .signup-band p { position: absolute; left: 91px; top: 24px; font-family: "Roboto", sans-serif; font-weight: 700; font-size: 15.5px; color: #fff; }
  .signup-button { position: absolute; left: 934px; top: 13px; width: 173px; height: 44px; border: 2px solid #fff; color: #fff; font-family: "Roboto", sans-serif; font-size: 16px; display: flex; align-items: center; justify-content: center; text-decoration: none; }

  .listing-tabs { position: absolute; top: 648px; left: 91px; display: flex; align-items: baseline; font-family: "Roboto", sans-serif; }
  .listing-tab { font-size: 17.5px; font-weight: 500; color: var(--heading); border-bottom: 2px solid #ccc; padding-bottom: 2px; }
  .see-all { margin-left: 25px; font-size: 13.5px; color: #444; }
  .see-all b { font-weight: 700; }
  .listing-tab--offers { margin-left: 28px; }
</style>
</head>
<body>
  <header class="site-header">
    <div class="brand">Brightquarry</div>
    <nav class="main-nav">
      <a class="is-active" href="#">Home</a>
      <a href="#">How It Works</a>
      <a href="#">Search</a>
      <a href="#">Members</a>
      <a href="#">Log In</a>
    </nav>
  </header>

  <section class="hero">
    <h1 class="hero-title">EASILY MAKE MORE MONEY</h1>
    <h2 class="hero-subtitle">JUST BY REFERRING YOURSELF, YOUR FRIENDS OR BUSINESS ASSOCIATES</h2>

    <article class="offer offer-1">
      <div class="offer-tile"><span role="img" aria-label="Icon of a person referring to four others"></span></div>
      <h3 class="offer-title">Make a referral to existing<br>advertiser</h3>
      <p class="offer-text">Earn up to $5000 when you make a successful<br>referral to one of our advertisers.</p>
      <a class="learn-more" href="#"><svg viewBox="0 0 16 16"><path d="M10 1l6 5.5-6 5.5V8.5C6 8.5 4 10 3 15 1.5 9.5 4 5 10 4.5z"/></svg>Learn More</a>
    </article>

    <article class="offer offer-2">
      <div class="offer-tile"><span role="img" aria-label="Icon of a magnifier over a group of people"></span></div>
      <h3 class="offer-title">Sign up a new business to offer<br>referral commisions to<br>ambassaadors</h3>
      <p class="offer-text">Earn up to $5000 or more when you earn 5% of<br>money paid out by business in referral fees.</p>
      <a class="learn-more learn-more--dark" href="#"><svg viewBox="0 0 16 16"><path d="M10 1l6 5.5-6 5.5V8.5C6 8.5 4 10 3 15 1.5 9.5 4 5 10 4.5z"/></svg>Learn More</a>
    </article>

    <article class="offer offer-3">
      <div class="offer-tile"><span role="img" aria-label="Icon of a group of people with an add sign"></span></div>
      <h3 class="offer-title">Sign up new<br>ambassadors</h3>
      <p class="offer-text">Earn up to $5000 or more when you earn 5% of<br>the money the ambassadors you sign up earn.</p>
      <a class="learn-more" href="#"><svg viewBox="0 0 16 16"><path d="M10 1l6 5.5-6 5.5V8.5C6 8.5 4 10 3 15 1.5 9.5 4 5 10 4.5z"/></svg>Learn More</a>
    </article>
  </section>

  <section class="payout">
    <span class="payout-label">Brightquarry has paid over</span>
    <span class="payout-amount">$359,465 YTD</span>
  </section>

  <section class="signup-band">
    <p>Brightquarry, Fastest Growing Referral Marketplace. Earn income just by referring people you know.</p>
    <a class="signup-button" href="#">Free to Sign Up!</a>
  </section>

  <nav class="listing-tabs">
    <span class="listing-tab">Categories</span>
    <span class="see-all"><b>+</b> See All Categories</span>
    <span class="listing-tab listing-tab--offers">Top Offers</span>
  </nav>
</body>
</html>
```